Velvet Harbor - Four rooms without doors

Front cover /artwork only for a cd that is to be released online.
The bands name is Velvet harbor they are alternative/indie band.
The albums title is "Four rooms without doors" (nothing to do with clocks please!)
Looking for a simple or striking image and band logo with album title.
The band is very 90s influenced so think grunge or Brit pop

```html
<!DOCTYPE html>
<html lang="en">
<head>
<meta charset="utf-8">
<title>Velvet Harbor – Four Rooms Without Doors</title>
<link rel="stylesheet" href="https://fonts.googleapis.com/css2?family=Cormorant+Garamond:wght@500;700&display=swap">
<style>
  :root {
    --ink-grey: #58575b;
    --title-white: #f4f2ee;
    --wash-orange: #d9783a;
    --wash-olive: #5f6a24;
    --wash-teal: #22808a;
    --wash-mist: #bcd8cc;
    --wash-pale: #e6ebe6;
    --field-green: #7f9a2a;
    --field-red: #a52d48;
    --road-green: #1d5236;
    --road-violet: #55245f;
  }

  html, body {
    margin: 0;
    padding: 0;
    width: 1200px;
    height: 1200px;
    overflow: hidden;
    background: #ffffff;
  }

  .album-cover {
    position: relative;
    width: 1200px;
    height: 1200px;
    overflow: hidden;
  }

  .cover-photo {
    position: absolute;
    inset: 0;
    background:
      radial-gradient(ellipse 38% 30% at 0% 27%, rgba(217,120,58,0.95), rgba(217,120,58,0) 70%),
      radial-gradient(ellipse 55% 38% at 12% 0%, rgba(95,106,36,0.95), rgba(95,106,36,0) 75%),
      radial-gradient(ellipse 60% 42% at 92% 4%, rgba(34,128,138,1), rgba(34,128,138,0) 75%),
      radial-gradient(ellipse 35% 28% at 100% 45%, rgba(240,240,242,0.95), rgba(240,240,242,0) 70%),
      radial-gradient(ellipse 50% 30% at 0% 88%, rgba(127,154,42,1), rgba(127,154,42,0) 72%),
      radial-gradient(ellipse 50% 32% at 100% 84%, rgba(165,45,72,1), rgba(165,45,72,0) 72%),
      radial-gradient(ellipse 38% 28% at 45% 100%, rgba(29,82,54,1), rgba(29,82,54,0) 75%),
      radial-gradient(ellipse 40% 26% at 88% 100%, rgba(85,36,95,1), rgba(85,36,95,0) 75%),
      linear-gradient(180deg, var(--wash-teal) 0%, var(--wash-mist) 42%, var(--wash-pale) 66%, #7a8f58 80%, #34473f 100%);
  }

  .grunge-texture {
    position: absolute;
    inset: 0;
    width: 1200px;
    height: 1200px;
    pointer-events: none;
  }

  .grunge-texture .grain { mix-blend-mode: overlay; opacity: 0.55; }
  .grunge-texture .scratches { mix-blend-mode: screen; opacity: 0.35; }
  .grunge-texture .mottle { mix-blend-mode: multiply; opacity: 0.3; }
  .grunge-texture .vignette { mix-blend-mode: multiply; }

  .band-name {
    position: absolute;
    left: 0;
    right: 0;
    top: 418px;
    margin: 0;
    text-align: center;
    font-family: "Cormorant Garamond", Georgia, serif;
    font-weight: 700;
    font-size: 168px;
    line-height: 1;
    letter-spacing: -0.005em;
    color: var(--ink-grey);
  }

  .album-title {
    position: absolute;
    left: 0;
    right: 0;
    top: 1060px;
    margin: 0;
    text-align: center;
    font-family: "Cormorant Garamond", Georgia, serif;
    font-weight: 500;
    font-size: 40px;
    line-height: 1;
    letter-spacing: 0.05em;
    text-transform: uppercase;
    color: var(--title-white);
  }
</style>
</head>
<body>
  <main class="album-cover">
    <div class="cover-photo" role="img" aria-label="Colour-washed photograph of an empty straight road running to a misty horizon between open fields, tinted orange, teal, green and magenta"></div>

    <svg class="grunge-texture" viewBox="0 0 1200 1200" aria-hidden="true">
      <defs>
        <filter id="fine-grain" x="0" y="0" width="100%" height="100%">
          <feTurbulence type="fractalNoise" baseFrequency="0.85" numOctaves="3" seed="4"/>
          <feColorMatrix type="saturate" values="0"/>
          <feComponentTransfer>
            <feFuncR type="linear" slope="1.8" intercept="-0.4"/>
            <feFuncG type="linear" slope="1.8" intercept="-0.4"/>
            <feFuncB type="linear" slope="1.8" intercept="-0.4"/>
          </feComponentTransfer>
        </filter>
        <filter id="paper-scratches" x="0" y="0" width="100%" height="100%">
          <feTurbulence type="fractalNoise" baseFrequency="0.004 0.22" numOctaves="2" seed="11"/>
          <feColorMatrix type="matrix" values="0 0 0 0 1  0 0 0 0 1  0 0 0 0 1  0 0 0 -6 4.1"/>
        </filter>
        <filter id="worn-mottle" x="0" y="0" width="100%" height="100%">
          <feTurbulence type="fractalNoise" baseFrequency="0.012" numOctaves="4" seed="7"/>
          <feColorMatrix type="saturate" values="0"/>
          <feComponentTransfer>
            <feFuncR type="linear" slope="2.2" intercept="-0.45"/>
            <feFuncG type="linear" slope="2.2" intercept="-0.45"/>
            <feFuncB type="linear" slope="2.2" intercept="-0.45"/>
          </feComponentTransfer>
        </filter>
        <radialGradient id="edge-burn" cx="50%" cy="50%" r="72%">
          <stop offset="55%" stop-color="#ffffff"/>
          <stop offset="100%" stop-color="#6c6a62"/>
        </radialGradient>
      </defs>
      <rect class="mottle" width="1200" height="1200" filter="url(#worn-mottle)"/>
      <rect class="grain" width="1200" height="1200" filter="url(#fine-grain)"/>
      <rect class="scratches" width="1200" height="1200" filter="url(#paper-scratches)"/>
      <rect class="vignette" width="1200" height="1200" fill="url(#edge-burn)"/>
    </svg>

    <h1 class="band-name">Velvet Harbor</h1>
    <p class="album-title">Four rooms without doors</p>
  </main>
</body>
</html>
```